Enhance the web site presence of Kolrith Global Limited

Upgrade the current web site www.kolrithpanel.com to share with the audience our current plan and future developments of our company. I have created a worksheet which shows all the pages that I like to have. The home page in English, Japanese and Chinese is hyperlinked to the various pages. Under the product, we should allow the user to select "single sided PCB or double sided PCB". The translation of the contents of the pages with Japanese is not complete but the English and Chinese are complete. You can download the briefing and photos in the dropbox files below;

https://www.sharelocker.net/sh/xk4trw92mpd3ab1/BBQm_Lp841zzPq2Rw7KtYnHjEa?dl=0

Target Market(s)

Electronic companies

Industry/Entity Type

Electronic

Coding

Coded - Design and coding required

Number of Pages Required

5+ page

Font styles to use
Sans Serif

Colors
00a990
0353a1
33b8a4

Requirements
Must have
• Get a sense of confidence on our company's integrity and capability to deliver the highest quality PCBs with the most competitive prices and best services. A sense of elegance is essential as we DON'T treat profits as the number one goal. Our number goal is to do the RIGHT things right. Having a mixture of our company photos will be appropriate.

```html
<!DOCTYPE html>
<html lang="en">
<head>
<meta charset="utf-8">
<title>Kolrith Global Limited</title>
<link href="https://fonts.googleapis.com/css2?family=Open+Sans:wght@400;600;700&family=Montserrat:wght@600;700&display=swap" rel="stylesheet">
<style>
:root{
  --blue:#0353a1;
  --teal:#00a990;
  --teal-light:#33b8a4;
  --navy:#0b3f86;
  --ink:#333a44;
  --muted:#6b7480;
  --rule:#e3e7ec;
  --band:#f1f3f5;
  --white:#ffffff;
}
*{box-sizing:border-box;margin:0;padding:0}
html,body{width:1200px;height:2776px;overflow:hidden}
body{font-family:"Open Sans",Arial,sans-serif;color:var(--ink);background:var(--white);position:relative}
h1,h2,h3{font-family:"Montserrat","Open Sans",sans-serif}
.btn{display:inline-block;background:var(--teal);color:var(--white);font-size:13px;font-weight:600;letter-spacing:.5px;padding:12px 26px;border-radius:3px;text-transform:uppercase}
.section-title{color:var(--blue);font-size:28px;font-weight:700;text-transform:uppercase;letter-spacing:.5px}
.title-rule{width:60px;height:3px;background:var(--teal);margin:14px auto 0}
.body-text{font-size:14px;line-height:1.75;color:var(--muted)}

/* top bar */
.topbar{position:absolute;top:0;left:0;width:1200px;height:34px;display:flex;justify-content:flex-end;align-items:center;gap:22px;padding-right:80px;font-size:12px;color:var(--muted)}
.topbar span{display:flex;align-items:center;gap:6px}
/* header */
.header{position:absolute;top:34px;left:0;width:1200px;height:78px;display:flex;align-items:center;padding:0 80px;justify-content:space-between}
.brand{display:flex;align-items:center;gap:10px}
.brand-mark{width:26px;height:26px;background:var(--blue)}
.brand-name{font-family:"Open Sans",sans-serif;font-weight:700;font-size:20px;color:var(--blue)}
.nav{display:flex;align-items:center;gap:30px;font-size:13px;font-weight:600;text-transform:uppercase;color:var(--ink)}
.nav .active{color:var(--blue);border-bottom:2px solid var(--blue);padding-bottom:4px}
.nav .login{background:var(--blue);color:var(--white);padding:9px 14px;border-radius:3px;font-size:12px}
/* hero */
.hero{position:absolute;top:112px;left:0;width:1200px;height:490px;background:linear-gradient(120deg,#5e8fb8 0%,#a9c3d6 40%,#7aa0b9 70%,#3f6f95 100%)}
.hero-text{position:absolute;top:250px;left:0;width:1200px;text-align:center;color:var(--white);text-shadow:0 2px 6px rgba(0,0,0,.35)}
.hero-text h1{font-size:38px;font-weight:700}
.hero-text p{font-family:"Montserrat",sans-serif;font-weight:700;font-size:22px;text-transform:uppercase;margin-top:10px;line-height:1.3}
.dots{position:absolute;top:530px;left:0;width:1200px;display:flex;justify-content:center;gap:8px}
.dots i{width:10px;height:10px;border-radius:50%;background:rgba(255,255,255,.55)}
.dots i.on{background:var(--white)}
/* welcome */
.welcome{position:absolute;top:640px;left:0;width:1200px;text-align:center}
.welcome .body-text{width:1000px;margin:26px auto 0}
.welcome .body-text + .body-text{margin-top:14px}
.welcome .btn{margin-top:26px}
/* single sided */
.single{position:absolute;top:940px;left:0;width:1200px;height:360px;background:var(--band)}
.single svg.slant{position:absolute;left:0;bottom:-20px}
.single-copy{position:absolute;left:80px;top:80px;width:560px}
.single-copy h2{color:var(--blue);font-size:26px;font-weight:700;text-transform:uppercase}
.single-copy .rule{width:60px;height:3px;background:var(--teal);margin:12px 0 18px}
.single-copy .btn{margin-top:22px}
.photo-single{position:absolute;left:705px;top:30px;width:420px;height:280px;background:linear-gradient(135deg,#d9dde1,#8f9aa4 60%,#c7cdd2);box-shadow:0 4px 12px rgba(0,0,0,.18)}
/* customers */
.customers{position:absolute;top:1340px;left:80px;width:1040px;height:100px;display:flex;align-items:center}
.customers h2{color:var(--ink);font-size:20px;font-weight:700;text-transform:uppercase;width:200px}
.arrows{position:absolute;left:0;top:66px;display:flex;gap:14px}
.logos{display:flex;gap:18px;margin-left:40px}
.logo-box{width:190px;height:84px;border:1px solid var(--rule);display:flex;align-items:center;justify-content:center;font-family:"Open Sans",sans-serif;font-weight:700;font-size:22px;color:var(--navy)}
/* double */
.photo-double{position:absolute;left:80px;top:1488px;width:580px;height:280px;background:linear-gradient(135deg,#b9c4cc,#6e7c86 55%,#cfd6db);box-shadow:0 4px 12px rgba(0,0,0,.18)}
.double-copy{position:absolute;left:700px;top:1530px;width:420px}
.double-copy h2{color:var(--blue);font-size:26px;font-weight:700;text-transform:uppercase}
.double-copy .rule{width:60px;height:3px;background:var(--teal);margin:12px 0 16px}
.double-copy .btn{margin-top:20px}
/* investment */
.invest{position:absolute;top:1880px;left:0;width:1200px;text-align:center}
.invest .body-text{width:960px;margin:26px auto 0}
.invest .btn{margin-top:26px}
/* locations */
.locations{position:absolute;top:2140px;left:0;width:1200px;height:430px;background:linear-gradient(180deg,#0d4c9a 0%,#08337a 100%)}
.locations h2{color:var(--white);font-size:26px;text-align:center;text-transform:uppercase;margin-top:48px}
.locations .title-rule{background:var(--teal-light)}
.loc-cols{position:absolute;top:160px;left:270px;display:flex;gap:110px}
.loc{width:340px;color:#d9e6f5;font-size:13px;line-height:1.8}
.loc h3{color:var(--white);font-size:16px;margin-bottom:8px}
.loc .row{display:flex;align-items:center;gap:8px}
/* footer */
.footer{position:absolute;top:2580px;left:0;width:1200px;height:196px;padding:30px 80px;display:flex;gap:60px;font-size:13px;color:var(--muted)}
.footer h4{color:var(--blue);font-size:13px;text-transform:uppercase;margin-bottom:10px}
.f-brand{width:260px}
.f-brand p{margin-top:12px;line-height:1.6;font-size:12px}
.sitemap ul{list-style:none;display:grid;grid-template-columns:110px 90px;gap:4px 10px}
.subscribe input{width:200px;height:34px;border:1px solid var(--rule);padding:0 10px;font-size:12px;font-family:inherit}
.subscribe .btn{padding:8px 20px;margin-top:10px;font-size:12px}
.social{display:flex;gap:10px}
.social i{width:26px;height:26px;background:var(--blue);border-radius:50%;display:block}
</style>
</head>
<body>

<div class="topbar">
  <span><svg width="12" height="12" viewBox="0 0 24 24"><path fill="#0353a1" d="M6.6 10.8a15 15 0 006.6 6.6l2.2-2.2a1 1 0 011-.25 11.4 11.4 0 003.6.57 1 1 0 011 1V20a1 1 0 01-1 1A17 17 0 013 4a1 1 0 011-1h3.5a1 1 0 011 1c0 1.25.2 2.45.57 3.57a1 1 0 01-.25 1z"/></svg>(852) 3100 4521</span>
  <span><svg width="13" height="10" viewBox="0 0 24 18"><rect x="1" y="1" width="22" height="16" fill="none" stroke="#0353a1" stroke-width="2"/><path d="M1 1l11 9 11-9" fill="none" stroke="#0353a1" stroke-width="2"/></svg>sales@kolrithpanel.com</span>
</div>

<header class="header">
  <div class="brand"><span class="brand-mark"></span><span class="brand-name">Kolrith Global</span></div>
  <nav class="nav">
    <span class="active">Home</span><span>Products</span><span>Our Facilities</span><span>Customers News</span><span>Quotes</span><span>Contact Us</span><span class="login">Customer Login</span>
  </nav>
</header>

<section class="hero" role="img" aria-label="Technician in a clean room working at a circuit board production line">
  <div class="hero-text">
    <h1>Kolrith Global Limited</h1>
    <p>We specialized in single &amp; double sized<br>printed circuit boards</p>
  </div>
  <div class="dots" style="top:418px"><i class="on"></i><i></i><i></i></div>
</section>

<section class="welcome">
  <h2 class="section-title">Welcome to our website</h2>
  <div class="title-rule"></div>
  <p class="body-text">Established in 2007, Kolrith Global Limited (KGL) is a Hong Kong company specializing in single and double sided printed circuit boards. Its manufacturing facility is located in a self-owned facility in Lianhe, Dongguan of China which is 50 minutes from Hong Kong.</p>
  <p class="body-text">Our mission is to become a premium low cost PCB supplier that fully embraces human, social and environmental responsibilities. Through our insatiable drive to maximize efficiency, KGL is becoming a highly efficient PCB factory with a capacity of 190,000 square meter a month. PCB is our business and it is through continued automation and innovation that we drive our growth in the next 10 years.</p>
  <span class="btn">Read more</span>
</section>

<section class="single">
  <div class="single-copy">
    <h2>Single sized printed circuit boards</h2>
    <div class="rule"></div>
    <p class="body-text">We are offering single layered circuit boards through our own production facility in China for customers in the audio and video industry, home appliance and camera, industrial equipment and power supply, automotive, as well as contract manufacturers.</p>
    <span class="btn">Read more</span>
  </div>
  <div class="photo-single" role="img" aria-label="Stacks of finished single sided circuit boards on the factory floor"></div>
  <svg class="slant" width="1200" height="40" viewBox="0 0 1200 40"><polygon points="0,0 1200,20 1200,28 0,8" fill="#00a990"/></svg>
</section>

<section class="customers">
  <h2>Our customers</h2>
  <div class="arrows">
    <svg width="12" height="18" viewBox="0 0 12 18"><path d="M10 2L3 9l7 7" fill="none" stroke="#333a44" stroke-width="2.5"/></svg>
    <svg width="12" height="18" viewBox="0 0 12 18"><path d="M2 2l7 7-7 7" fill="none" stroke="#333a44" stroke-width="2.5"/></svg>
  </div>
  <div class="logos">
    <div class="logo-box">Norvale</div>
    <div class="logo-box">Taskura</div>
    <div class="logo-box">Quintel</div>
    <div class="logo-box">Velmora</div>
  </div>
</section>

<div class="photo-double" role="img" aria-label="Double layered circuit boards moving along an automated conveyor"></div>
<section class="double-copy">
  <h2>Double layered printed circuit boards</h2>
  <div class="rule"></div>
  <p class="body-text">We are offering two layered and multi-layered circuit boards for our customers through our strategically approved printed circuit boards manufacturers. With our own QC for double sided and multi-layered circuit boards, we work with a number of strategically approved manufacturers.</p>
  <span class="btn">Read more</span>
</section>

<section class="invest">
  <h2 class="section-title">Our investment &amp; upgrade</h2>
  <div class="title-rule"></div>
  <p class="body-text">Maintaining a highly automated factory is the only way to ensure consistent product and long-term competitive efficiency. From 2015 to 2017, KGL invested over US$3.5 million in automating our production and quality control process and enhancing our environmental processing facility.</p>
  <span class="btn">Read more</span>
</section>

<section class="locations">
  <h2>Our business locations</h2>
  <div class="title-rule"></div>
  <div class="loc-cols">
    <div class="loc">
      <h3>Our Hong Kong Business Address</h3>
      <p>Kolrith Global Limited</p>
      <p>Unit 9, Harbourview Centre</p>
      <p>18 Marlow Street</p>
      <p>Kwun Tong, Hong Kong</p>
      <p class="row">T: +852 3100 4521 &nbsp; F: +852 3100 4522</p>
      <p class="row">sales@kolrithpanel.com</p>
    </div>
    <div class="loc">
      <h3>Our China Business Address</h3>
      <p>Kolrith Global (Dongguan) Limited</p>
      <p>No. 6 Fenglin Road</p>
      <p>Lianhe Industrial District</p>
      <p>Dongguan, Guangdong Province</p>
      <p class="row">T: +86 769 8200 4410 &nbsp; F: +86 769 8200 4411</p>
    </div>
  </div>
</section>

<footer class="footer">
  <div class="f-brand">
    <div class="brand"><span class="brand-mark"></span><span class="brand-name">Kolrith Global</span></div>
    <p>Copyright © 2018 Kolrith Global Limited.<br>All Rights Reserved.</p>
  </div>
  <div class="sitemap">
    <h4>Site Map</h4>
    <ul><li>Home</li><li>News</li><li>Products</li><li>Quotes</li><li>Our Facilities</li><li>Contact Us</li><li>Customers</li></ul>
  </div>
  <div class="subscribe">
    <h4>Email Subscribe</h4>
    <input type="text" placeholder="Enter Email Address"><br>
    <span class="btn">Sign up</span>
  </div>
  <div>
    <h4>Follow Us</h4>
    <div class="social"><i></i><i></i><i></i><i></i></div>
  </div>
</footer>

</body>
</html>
```